Creation of an E Book on Business Risk

I have the Copy... I would like this copy to be made into an interesting ebook - with Pictures that are relevant to the topic.

You also need to include the Vell Logo's and Colour schemes as per attached other brochures

Hi
I am looking for the same theme as the previous ebook "steps to grow savings inside your trust fund"

HEADING PAGE
How to protect your business from risk

with a picture that portrays the sentence

PART 2 Disclaimer and contents
clean and simple
(same as

PART 3 Bsns is Personal anfd ... family's future..

PART 4 Buy Sell and Case Studies

etc...

Each Part should have an awesome Picture that relates to the subject

thanks
Milo

Target Market(s)

Small to Medium Size Businesses that need to protect themselves from unforeseen events

Industry/Entity Type

Business

Requirements
Must have
• THe Brochure must have all the copy, and flow with pictures that are relevant to the theme

```html
<!DOCTYPE html>
<html lang="en">
<head>
<meta charset="utf-8">
<title>Business Risk – Buy / Sell Agreements</title>
<link href="https://fonts.googleapis.com/css2?family=Noto+Sans:wght@400;700&family=Gelasio:wght@400;700&family=Oswald:wght@400;500&display=swap" rel="stylesheet">
<style>
  :root {
    --band: #2b8fd4;
    --page: #f3f3f3;
    --ink: #0e4f7e;
    --heading-blue: #16669f;
    --orange: #f7941d;
    --card-top: #69b6f3;
    --card-bottom: #3a8de0;
    --card-edge: #2f7fcf;
    --dark: #0a1e30;
  }
  * { margin: 0; padding: 0; box-sizing: border-box; }
  html, body { width: 1200px; height: 1078px; overflow: hidden; }
  body { background: var(--band); font-family: "Noto Sans", sans-serif; color: var(--ink); position: relative; }
  h2, h3 { font-weight: 400; }
  .page { position: absolute; left: 24px; top: 0; width: 1143px; height: 1078px; background: var(--page); }
  .abs { position: absolute; }

  .stats { position: absolute; left: 32px; top: 10px; width: 730px; list-style: none; font-size: 14px; line-height: 20px; }
  .stats li { position: relative; padding-left: 21px; margin-bottom: 8.5px; }
  .stats li::before { content: ""; position: absolute; left: 0; top: 6px; border-left: 7px solid var(--orange); border-top: 4.5px solid transparent; border-bottom: 4.5px solid transparent; }

  .photo { position: absolute; background: linear-gradient(135deg, #dfe4e8, #7d8790 55%, #2c3238); }
  .photo-exec { left: 758px; top: 0; width: 359px; height: 285px; }

  .family-title { left: 29px; top: 257px; font-family: "Gelasio", serif; font-weight: 400; font-size: 28px; line-height: 34px; color: var(--orange); white-space: nowrap; }
  .dashed { left: 27px; top: 300px; width: 1088px; border-top: 1.5px dashed #555; }

  .intro { left: 27px; top: 326px; width: 1100px; font-size: 14px; line-height: 20.4px; }
  .intro p { margin-bottom: 8.4px; }

  .section-title { left: 24px; top: 557px; font-family: "Oswald", sans-serif; font-weight: 500; font-size: 23px; line-height: 32px; color: var(--heading-blue); white-space: nowrap; }
  .dotted { left: 241px; top: 581px; width: 875px; border-top: 2px dotted var(--heading-blue); }

  .q-button { position: absolute; width: 143px; height: 49px; border-radius: 4px; border: 1px solid #2a86c4;
    background: linear-gradient(#a9e0fa, #5cc2f2 50%, #37aee8); display: flex; align-items: center; padding-left: 19px;
    font-weight: 700; font-size: 25px; color: var(--dark); letter-spacing: .5px; }
  .q-button svg { margin-left: 4px; }
  .why { left: 23px; top: 607px; }
  .what { left: 23px; top: 924px; }

  .motto { left: 187px; top: 613px; font-family: "Gelasio", serif; font-weight: 400; font-size: 28px; line-height: 34px; color: var(--orange); white-space: nowrap; }
  .exits { left: 24px; top: 667px; font-family: "Gelasio", serif; font-weight: 700; font-size: 18.5px; line-height: 24px; color: var(--heading-blue); white-space: nowrap; }

  .exit-card { position: absolute; top: 720px; width: 539px; height: 172px; border: 1px solid var(--card-edge); border-radius: 4px;
    background: linear-gradient(var(--card-top), var(--card-bottom)); color: #fff; font-weight: 700; font-size: 14px; line-height: 20.4px; padding: 20px 0 0 13px; }
  .exit-card p { width: 320px; margin-bottom: 9px; }
  .exit-card b { color: var(--dark); }
  .voluntary { left: 23px; }
  .involuntary { left: 579px; }
  .card-photo { position: absolute; top: 15px; right: 18px; width: 175px; height: 141px; border: 2px solid #cfe6f7; border-radius: 3px; }
  .voluntary .card-photo { background: radial-gradient(circle, #fff6c9, #f5c850 70%, #e3a830); }
  .involuntary .card-photo { background: linear-gradient(90deg, #f1f4f0, #c9d3cf 60%, #8e9a98); }

  .definition { left: 27px; top: 990px; width: 1100px; font-size: 13.8px; line-height: 20.4px; }
  .sub-title { left: 27px; top: 1055px; font-family: "Gelasio", serif; font-weight: 700; font-size: 17px; line-height: 22px; color: var(--heading-blue); }
</style>
</head>
<body>
<main class="page">
  <ul class="stats">
    <li>35% plan to retire in between 5 and 10 years</li>
    <li>19.3% have a succession plan for the CEO</li>
    <li>85% do not have formal succession plan,&nbsp; but 31% are in the process of developing&nbsp; one</li>
    <li>The probability of at least one partner dying before the age of 65 for a two-partner business structure is a significant 34%, climbing to 71% if your business has six partners1.</li>
    <li>The chance of a partner becoming disabled is even higher with 51% likelihood for a two-partner business structure, and 88% for a business with six partners2.</li>
  </ul>
  <div class="photo photo-exec" role="img" aria-label="Businessman in a suit working on a laptop"></div>

  <h2 class="abs family-title">It’s not just your business’s future, but also your family’s</h2>
  <div class="abs dashed"></div>

  <section class="abs intro">
    <p>Many business principals do not hesitate to insure physical assets such as motor vehicles, plant and equipment, however they offer fail to insure the most important aspect to revenue generation and decision making: themselves and their key staff.</p>
    <p>This oversight can not only be costly to the business, but the families of those involved.</p>
    <p>Businesses are similar to individuals. They have assets, debts, income and expenses.&nbsp; In the event of a long term absence of a key income generator or decision maker in the business, how will your business survive?</p>
    <p>Here are some common issues in many businesses, with real and viable solutions to assist your business and more importantly, protect your family and other assets in the loss of a owner / director or staff in your business.</p>
  </section>

  <h2 class="abs section-title">BUY/ SELL AGREEMENTS</h2>
  <div class="abs dotted"></div>

  <div class="q-button why">WHY<svg width="30" height="40" viewBox="0 0 30 40"><path d="M5 12 Q5 3 15 3 Q26 3 26 12 Q26 18 19 21 Q16 23 16 27" fill="none" stroke="#fff" stroke-width="6" stroke-linecap="round"/><circle cx="16" cy="35" r="3.8" fill="#fff"/></svg></div>
  <h2 class="abs motto">People don’t plan to fail, they fail to plan</h2>
  <h3 class="abs exits">Exits can be voluntary or involuntary.</h3>

  <div class="exit-card voluntary">
    <p><b>VOLUNTARY EXIT</b> occur when a business owner leaves a business on his or her own terms.</p>
    <p><b>EXAMPLE:</b> A business owner successfully passes on their share of the business via a management buy in.</p>
    <div class="card-photo" role="img" aria-label="Two businessmen shaking hands"></div>
  </div>
  <div class="exit-card involuntary">
    <p><b>INVOLUNTARY EXIT</b> occur when a business owner leaves a business suddenly and unexpectedly.</p>
    <p><b>EXAMPLE:</b> A business owner sis involved in a car accident that leaves them totally and permanently disabled.</p>
    <div class="card-photo" role="img" aria-label="Patient in a wheelchair in a hospital corridor"></div>
  </div>

  <div class="q-button what">WHAT<svg width="30" height="40" viewBox="0 0 30 40"><path d="M5 12 Q5 3 15 3 Q26 3 26 12 Q26 18 19 21 Q16 23 16 27" fill="none" stroke="#fff" stroke-width="6" stroke-linecap="round"/><circle cx="16" cy="35" r="3.8" fill="#fff"/></svg></div>
  <p class="abs definition">A buy sell agreement is a legal contract between business principals which documents what will happen in the event of on of the owners experiences a traumatic event, is totally or permanently Disabled or dies.&nbsp; It is a Will for the business.&nbsp; It will comprise of two components:</p>
  <h3 class="abs sub-title">A Transfer Agreement:</h3>
</main>
</body>
</html>
```